Women Web Portal

We are developing an internet portal with content created by and for women in Latin America.
This portal will contain different categories focused on relevant topics for women who are at the same time mothers, lovers, workers, pet-owners, ...

We are looking for design that are at the same time uncluttered, easy-to-use and obvious, and comfy. Pastel colours, buttons using traditional fonts, large space for pictures, highlighted social elements,...

Our target being the middle-class women, we want a design that feels comfortable, real, a bit trendy and traditional, not a Tarsk & Welmore design, something women can relate to and feel comfortable enough to come back and participate.

Examples of websites:
www.dishtable.example
mujer.qelvo.example
www.cabellorinva.example
www.fourneau.example
Updates

Hi dear designers. After viewing some first drafts, I have updated the brief so you might have a better understanding of what we are looking for.

Thanks

Reason: We've been away for a while, unavailable to provide adequate feedback to the designs already sent. So we're extending the deadline in order to give time to everyone to adapt their work according to the feedback we'll be providing today.

Target Market(s)

Women between 25 and 50 years from Latin America. Mainly mothers: basically, we want women to interact with each other and with the content of the site so they create a strong community.

Advertisingly speaking, we want to have users, contents and FMCG brands to live together on this website.

Industry/Entity Type

Internet

Requirements
Must have
• Pastel colours for category tabs. Comfortable look & feel.

The design should include 3 different pages:
- Homepage
- Article page
- User profile

The page will be done in responsive design, so design should be thought to be adapted according to the browser (2 or 3 columns).

Thanks for doing it as a PSD file .

The design should also include:
- 8 category tabs
- Space for 728x90px and 300x600px advertising format.
- A relevant menu bar at the beginning of each page
Nice to have
• News feed/best content/most active comments zone: we need to bring forward content to our users so they'll be attracted to visit more pages of the website.

Small format to register (account).

Slider or any other moving objects.

Any idea that would facilitate and increase user participation
Should not have
• Actual text. please use Lorem Ipsum.

```html
<!DOCTYPE html>
<html lang="en">
<head>
<meta charset="utf-8">
<title>Women Portal – Home</title>
<link rel="stylesheet" href="https://fonts.googleapis.com/css2?family=Linden+Hill&family=Open+Sans:wght@400&display=swap">
<style>
:root{
  --berry:#9c2a54;
  --berry-soft:rgba(160,36,80,.82);
  --ink:#3a3a3a;
  --muted:#6a6a6a;
  --rule:#d8d8d8;
  --icon:#555555;
  --bg:#ffffff;
  --ad-red:#a0222a;
}
*{margin:0;padding:0;box-sizing:border-box}
html,body{width:1200px;height:1200px;overflow:hidden;background:var(--bg)}
body{position:relative;font-family:"Linden Hill",Georgia,serif;color:var(--ink)}
.abs{position:absolute}

/* header */
.brand-mark{left:142px;top:44px;width:66px;height:60px;border-radius:50%;background:radial-gradient(circle at 40% 40%,#f6c23a,#e88bb0 60%,#8cc63e)}
.brand-name{left:232px;top:44px;font-size:30px;color:var(--berry)}
.brand-tag{left:234px;top:79px;font-family:"Open Sans",sans-serif;font-size:14px;color:var(--muted)}
.search{left:914px;top:31px;width:23px;height:23px}
.account{left:958px;top:33px;font-size:14px;color:var(--muted);display:flex;gap:13px}
.account span+span{border-left:1px solid var(--rule);padding-left:13px}
.menu{right:136px;top:87px;display:flex;font-size:14px;color:var(--muted)}
.menu li{list-style:none;padding:0 13px;border-left:1px solid var(--rule)}
.menu li:first-child{border:0;color:var(--berry)}
.menu li:last-child{padding-right:0}

/* hero */
.hero{left:0;top:138px;width:1200px;height:396px;background:linear-gradient(90deg,#8e1a1e 0%,#b8383c 30%,#a04a3e 55%,#d8b09a 72%,#7a5a48 100%)}
.hero-panel{left:143px;top:138px;width:386px;height:358px;background:var(--berry-soft);color:#fff;padding:62px 0 0 61px}
.hero-panel h1{font-weight:400;font-size:36px;margin-bottom:28px}
.hero-panel p{font-size:21px;line-height:26px}
.hero-panel .byline{margin-top:48px}
.slide-arrow{top:299px;width:34px;height:34px}

/* features */
.feature{top:563px;width:245px}
.num{position:absolute;left:-50px;top:0;width:36px;height:36px;border-radius:50%;background:var(--berry);color:#fff;font-size:24px;text-align:center;line-height:36px}
.feature h2{font-weight:400;font-size:18px;margin:7px 0 16px;white-space:nowrap}
.feature p{font-size:13px;line-height:16px;color:var(--ink)}
.more{top:693px;font-size:14px;color:var(--berry);display:flex;align-items:center;gap:10px}
.chev{width:14px;height:14px;display:block}

/* sections */
.section-title{font-size:21px;color:var(--berry)}
.rule{height:1px;background:var(--rule)}
.photo{top:802px;width:196px;height:120px}

.ad-head{left:237px;top:980px;width:226px;height:90px;background:var(--ad-red);color:#fff;font-size:26px;line-height:32px;padding:13px 0 0 16px}
.ad-photo{left:463px;top:980px;width:288px;height:90px;background:linear-gradient(90deg,#d7d4cf,#ece9e4 50%,#c9c3bc)}
.ad-brand{left:762px;top:998px;display:flex;align-items:center;gap:8px;font-size:26px;color:#222}
.ad-brand i{width:34px;height:34px;border-radius:50%;background:var(--ad-red);display:block}
.ad-url{left:762px;top:1044px;font-size:11px;letter-spacing:2px;color:#222}

.col-head{top:1174px;width:260px;font-size:17px;line-height:20px;border-bottom:1px solid var(--rule);padding-bottom:2px}
</style>
</head>
<body>
<header>
  <div class="abs brand-mark" aria-hidden="true"></div>
  <div class="abs brand-name">Company name</div>
  <div class="abs brand-tag">your tagline goes here</div>
  <svg class="abs search" viewBox="0 0 23 23" aria-label="Search"><circle cx="11.5" cy="11.5" r="11.5" fill="#9c2a54"/><circle cx="10.5" cy="10.5" r="3.5" fill="none" stroke="#fff" stroke-width="1.5"/><line x1="13" y1="13" x2="16" y2="16" stroke="#fff" stroke-width="1.5"/></svg>
  <div class="abs account"><span>Log In</span><span>Register</span></div>
  <ul class="abs menu"><li>Menu 1</li><li>Menu 2</li><li>Menu 3</li><li>Menu 4</li><li>Menu 5</li><li>Menu 6</li><li>Menu 7</li><li>Menu 8</li></ul>
</header>

<section>
  <div class="abs hero" role="img" aria-label="Photo of a smiling woman resting on a red sofa"></div>
  <div class="abs hero-panel">
    <h1>Architecto archit</h1>
    <p>Fugit aut illo omnis explicabo<br>Ipsa ipsa, nemo rem ipsam<br>Quasi illo dolores ut voluptatem<br>Doloremque perspiciatis</p>
    <p class="byline">Beatae Magni</p>
  </div>
  <svg class="abs slide-arrow" style="left:33px" viewBox="0 0 34 34" aria-label="Previous"><circle cx="17" cy="17" r="17" fill="#9c2a54"/><path d="M20 10l-7 7 7 7" fill="none" stroke="#fff" stroke-width="2.5"/></svg>
  <svg class="abs slide-arrow" style="left:1131px" viewBox="0 0 34 34" aria-label="Next"><circle cx="17" cy="17" r="17" fill="#9c2a54"/><path d="M14 10l7 7-7 7" fill="none" stroke="#fff" stroke-width="2.5"/></svg>
</section>

<section>
  <div class="abs feature" style="left:220px"><span class="num">1</span><h2>Lorem ipsum dolar sit</h2><p>Fugit aut illo omnis explicabo ipsa ipsa, nemo rem ipsam quasi illo dolores ut voluptatem doloremque perspiciatis beatae magni architecto odit odit, aspernatur magni</p></div>
  <div class="abs feature" style="left:511px"><span class="num">2</span><h2>Voluptatem doloremque</h2><p>Voluptas aut sit odit quasi quasi, unde quae ratione inventore ipsa explicabo iste sunt sed ipsam voluptatem consequuntur iste ipsam ipsam consequuntur</p></div>
  <div class="abs feature" style="left:806px;width:230px"><span class="num">3</span><h2>Sed enim accusantium</h2><p>Sed enim accusantium laudantium sunt perspiciatis ipsam sed doloremque ipsam dolores totam unde unde, et aut illo aut veritatis explicabo dicta quia dicta</p></div>
  <div class="abs more" style="left:335px">Veritatis unde <svg class="chev" viewBox="0 0 14 14"><circle cx="7" cy="7" r="7" fill="#555"/><path d="M6 4l3 3-3 3" fill="none" stroke="#fff" stroke-width="1.6"/></svg></div>
  <div class="abs more" style="left:650px">Sed enim <svg class="chev" viewBox="0 0 14 14"><circle cx="7" cy="7" r="7" fill="#555"/><path d="M6 4l3 3-3 3" fill="none" stroke="#fff" stroke-width="1.6"/></svg></div>
  <div class="abs more" style="left:928px">Omnis ipsa <svg class="chev" viewBox="0 0 14 14"><circle cx="7" cy="7" r="7" fill="#555"/><path d="M6 4l3 3-3 3" fill="none" stroke="#fff" stroke-width="1.6"/></svg></div>
</section>

<section>
  <div class="abs section-title" style="left:184px;top:739px">Accusantium laudantium</div>
  <div class="abs rule" style="left:419px;top:753px;width:536px"></div>
  <svg class="abs chev" style="left:985px;top:746px" viewBox="0 0 14 14" aria-label="Previous"><circle cx="7" cy="7" r="7" fill="#555"/><path d="M8 4l-3 3 3 3" fill="none" stroke="#fff" stroke-width="1.6"/></svg>
  <svg class="abs chev" style="left:1003px;top:746px" viewBox="0 0 14 14" aria-label="Next"><circle cx="7" cy="7" r="7" fill="#555"/><path d="M6 4l3 3-3 3" fill="none" stroke="#fff" stroke-width="1.6"/></svg>
  <div class="abs photo" style="left:183px;background:linear-gradient(135deg,#c9d3dc,#e48aa8 55%,#d8cbb8)" role="img" aria-label="Photo of a mother hugging her daughter on a beach"></div>
  <div class="abs photo" style="left:396px;background:linear-gradient(135deg,#5a1a14,#d8302e 50%,#e6b15a)" role="img" aria-label="Photo of two women laughing over coffee"></div>
  <div class="abs photo" style="left:608px;background:linear-gradient(135deg,#e6e2dc,#c79a78 50%,#f1eee9)" role="img" aria-label="Photo of three women friends together outdoors"></div>
  <div class="abs photo" style="left:821px;background:linear-gradient(135deg,#f2f0ee,#b8825e 50%,#dfe4ea)" role="img" aria-label="Photo of a family gathered around a laptop"></div>
</section>

<aside>
  <div class="abs ad-head">Lorem ipsum dolor<br>sit amet daily.</div>
  <div class="abs ad-photo" role="img" aria-label="Photo of a reader holding a printed paper"></div>
  <div class="abs ad-brand"><i></i>Pressline Guild</div>
  <div class="abs ad-url">www.pressline.example</div>
</aside>

<section>
  <div class="abs section-title" style="left:184px;top:1113px">Voluptatem consequntur</div>
  <div class="abs rule" style="left:417px;top:1128px;width:599px"></div>
  <div class="abs col-head" style="left:183px">laudantium laudantium sunt</div>
  <div class="abs col-head" style="left:475px">Dolar sit amet voluptatem</div>
  <div class="abs col-head" style="left:764px">Doloremque perspiciatis beatae</div>
</section>
</body>
</html>
```